Wine Label Redesign For California Wine Company

We’re looking to refresh our brand with a new professional looking label. We love what we have and was well received over the past three years and would like to keep a couple of the element: Name (Marco Vellin), it doesn’t have to be in cursive. The swirl, this how everybody recognizes our brand as it’s also in our logo. Colors: Gold and whatever you think is awesome. Looking forward to seeing your work.

Target Market(s)

Retailers

Industry/Entity Type

Winery

Font styles to use
Serif
Script

Colors

Designer to choose colors to be used in the design.

Requirements
Must have
• Front Label:
• Symphony (Varietal)
• 2016 (vintage)
• Lodi, California (location)
• Marco Vellin (Name)
• Back Label:
• Government Warning
• www.vellinwineco-example.com (website)
• 2016 (vintage)
• Swirl
Nice to have
• Creativity
• Bold colors
• Something that pops
Should not have
• Should not look nothing like my old label.

```html
<!DOCTYPE html>
<html lang="en">
<head>
<meta charset="utf-8">
<title>Symphony – Wine Labels</title>
<link rel="stylesheet" href="https://fonts.googleapis.com/css2?family=Cinzel:wght@400;700&family=Marcellus&display=swap">
<style>
  :root {
    --backdrop: #bdb5b1;
    --label-black: #050505;
    --gold: #d9b43c;
    --gold-deep: #a88a2a;
    --gold-line: #b8952f;
    --cream: #f1ebe0;
    --cream-warm: #e4d6c2;
    --ink: #111111;
    --white: #f4f4f4;
  }
  * { box-sizing: border-box; margin: 0; padding: 0; }
  html, body { width: 880px; height: 1200px; overflow: hidden; }
  body {
    background: var(--backdrop);
    position: relative;
    font-family: "Marcellus", serif;
  }
  .label {
    position: absolute;
    top: 375px;
    width: 380px;
    height: 449px;
    background: var(--label-black);
  }
  .label--front { left: 40px; }
  .label--back { left: 460px; }

  .label__head {
    position: absolute; left: 0; top: 0; width: 100%; height: 66px;
    display: flex; align-items: center; justify-content: center;
  }
  .varietal {
    font-family: "Cinzel", serif;
    color: var(--gold);
    font-size: 30px;
    letter-spacing: 8px;
    padding-left: 8px;
  }
  .label__body {
    position: absolute; left: 0; top: 66px; width: 100%; height: 289px;
    border-top: 2px solid var(--gold-line);
    border-bottom: 2px solid var(--gold-line);
    background: linear-gradient(90deg, var(--cream-warm) 0%, var(--cream) 35%, #fbf8f2 55%, var(--cream) 75%, var(--cream-warm) 100%);
  }
  .label__foot {
    position: absolute; left: 0; top: 355px; width: 100%; height: 94px;
    display: flex; flex-direction: column; align-items: center; justify-content: center;
  }
  .origin {
    font-family: "Marcellus", serif;
    color: var(--gold);
    font-size: 23px;
    letter-spacing: 3px;
    padding: 3px 2px 2px;
    border-top: 1px solid var(--gold-line);
    border-bottom: 1px solid var(--gold-line);
  }
  .vintage {
    color: var(--white);
    font-size: 13px;
    letter-spacing: 7px;
    padding-left: 7px;
    margin-top: 8px;
  }

  /* front */
  .house-name--vertical {
    position: absolute;
    left: 62px; top: 150px;
    transform: translate(-50%, -50%) rotate(-90deg);
    white-space: nowrap;
    font-family: "Marcellus", serif;
    font-size: 34px;
    color: var(--ink);
    letter-spacing: 1px;
  }
  .emblem-area {
    position: absolute;
    left: 140px; top: 40px;
    width: 200px; height: 220px;
  }

  /* back */
  .brand-line {
    display: flex; align-items: center; gap: 12px;
  }
  .brand-line__name {
    font-family: "Marcellus", serif;
    font-size: 26px;
    color: var(--gold);
  }
  .brand-line__dot {
    width: 26px; height: 26px; border-radius: 50%;
    background: var(--gold);
  }
  .warning {
    position: absolute; left: 0; top: 16px; width: 100%;
    text-align: center;
    color: var(--ink);
    font-size: 12.6px;
    line-height: 19px;
    letter-spacing: 0.5px;
    text-transform: uppercase;
  }
  .warning__title {
    font-family: "Cinzel", serif;
    font-weight: 700;
    font-size: 14px;
    letter-spacing: 0.5px;
  }
  .warning p { padding: 0 36px; }
  .warning p + p { margin-top: 8px; }
  .facts {
    position: absolute; left: 18px; right: 18px; top: 205px;
    display: flex; justify-content: space-between;
    font-family: "Cinzel", serif; font-weight: 700;
    font-size: 12px; color: var(--ink);
  }
  .website {
    position: absolute; left: 62px; right: 62px; top: 232px;
    text-align: center;
    font-family: "Cinzel", serif; font-weight: 700;
    font-size: 10.5px; letter-spacing: 2.6px;
    color: var(--ink);
    padding: 4px 0;
    border-top: 1px solid #6b6256;
    border-bottom: 1px solid #6b6256;
  }
</style>
</head>
<body>

  <section class="label label--front" aria-label="Front label">
    <header class="label__head"><h1 class="varietal">SYMPHONY</h1></header>
    <div class="label__body" role="img" aria-label="Cream damask patterned background">
      <span class="house-name--vertical">Marco Vellin</span>
      <svg class="emblem-area" viewBox="0 0 200 220" role="img" aria-label="Brand emblem area">
        <defs>
          <radialGradient id="emblemGold" cx="45%" cy="40%" r="60%">
            <stop offset="0" stop-color="#e6c84a"/>
            <stop offset="1" stop-color="#7d6a2a"/>
          </radialGradient>
        </defs>
        <circle cx="100" cy="115" r="80" fill="url(#emblemGold)"/>
      </svg>
    </div>
    <footer class="label__foot">
      <div class="origin">Lodi, California</div>
      <div class="vintage">2016</div>
    </footer>
  </section>

  <section class="label label--back" aria-label="Back label">
    <header class="label__head">
      <div class="brand-line">
        <span class="brand-line__name">Marco Vellin</span>
        <span class="brand-line__dot"></span>
      </div>
    </header>
    <div class="label__body" role="img" aria-label="Cream damask patterned background">
      <div class="warning">
        <div class="warning__title">Government Warning:</div>
        <p>(1) According to the Surgeon General, women should not drink alcoholic beverages during pregnancy because of the risk of birth defects.</p>
        <p>(2) Consumption of alcoholic beverages impairs your ability to drive a car or operate machinery, and may cause health problems.</p>
      </div>
      <div class="facts">
        <span>CONTAINS SULFITES</span>
        <span>ALC 14.2% BY VOL</span>
        <span>750ML</span>
      </div>
      <div class="website">WWW.VELLINWINECO-EXAMPLE.COM</div>
    </div>
    <footer class="label__foot">
      <div class="origin">Lodi, California</div>
      <div class="vintage">2016</div>
    </footer>
  </section>

</body>
</html>
```